Breezeway Comfort business cards design

Need a business card design for a Heating and Air Conditioning business. I need these items included.
Business name: Breezeway Comfort
Owner: Marcus Tollefsen
License # 2874590
Phone number # 555-382-4071
Email: breezewaycomfortair@mailvista.example
Sales
Service
Installation
Maintenance

Heating and Air Conditioning

Requirements
Must have
• Company name , license number , phone number , email

```html
<!DOCTYPE html>
<html lang="en">
<head>
<meta charset="utf-8">
<title>Breezeway Comfort business cards</title>
<link rel="stylesheet" href="https://fonts.googleapis.com/css2?family=Krona+One&family=Arimo:wght@400;700&display=swap">
<style>
  :root {
    --brand-blue: #0b3aa6;
    --brand-blue-deep: #082f8c;
    --pattern-blue: #1450c8;
    --accent-orange: #f5822a;
    --accent-red: #e8334a;
    --name-orange: #f15a3a;
    --ink-white: #ffffff;
    --paper: #ffffff;
    --backdrop: #e9ebef;
  }
  * { box-sizing: border-box; margin: 0; padding: 0; }
  html, body { width: 1200px; height: 874px; overflow: hidden; }
  body {
    background: var(--backdrop);
    font-family: "Arimo", Arial, sans-serif;
    position: relative;
  }
  .card {
    position: absolute;
    left: 280px;
    width: 640px;
    height: 366px;
    border-radius: 20px;
    overflow: hidden;
    box-shadow: 0 10px 28px rgba(20, 30, 60, 0.22);
  }

  /* Back of card */
  .card-back { top: 47px; background: var(--brand-blue); }
  .card-back .pattern-field {
    position: absolute; inset: 0;
    background: radial-gradient(ellipse at 70% 40%, var(--pattern-blue) 0%, var(--brand-blue) 70%);
  }
  .services {
    position: absolute; left: 40px; bottom: 50px;
    display: flex; align-items: center; gap: 12px;
    color: var(--ink-white);
    font-size: 14px; letter-spacing: 0.4px;
    white-space: nowrap;
  }
  .services .dot {
    width: 6px; height: 6px; border-radius: 50%;
    background: var(--accent-orange);
  }
  .back-mark {
    position: absolute; right: 26px; bottom: 26px;
    display: flex; align-items: center; gap: 6px;
    color: var(--ink-white);
    font-family: "Krona One", Arial, sans-serif;
    font-size: 9px;
    white-space: nowrap;
  }
  .back-mark .mark-dot {
    width: 12px; height: 12px; border-radius: 50%;
    background: var(--accent-orange);
  }

  /* Front of card */
  .card-front { top: 461px; background: var(--paper); }
  .front-brand {
    position: absolute; left: 0; top: 0; width: 270px; height: 100%;
    display: flex; align-items: center; justify-content: center; gap: 10px;
  }
  .front-brand .brand-dot {
    width: 22px; height: 22px; border-radius: 50%;
    background: var(--accent-orange);
    flex: none;
  }
  .front-brand .brand-name {
    font-family: "Krona One", Arial, sans-serif;
    font-size: 19px;
    color: var(--brand-blue);
    line-height: 1.25;
  }
  .divider {
    position: absolute; left: 270px; top: 0; width: 8px; height: 100%;
    background: linear-gradient(180deg, var(--accent-red), var(--accent-orange) 55%, var(--accent-red));
  }
  .contact-panel {
    position: absolute; left: 278px; top: 0; right: 0; height: 100%;
    background: var(--brand-blue);
    color: var(--ink-white);
    padding: 78px 20px 0 30px;
  }
  .owner-name {
    font-family: "Krona One", Arial, sans-serif;
    font-size: 23px;
    color: var(--name-orange);
    letter-spacing: 0.2px;
    white-space: nowrap;
  }
  .owner-role { font-size: 15px; margin-top: 4px; }
  .license { font-size: 16px; margin-top: 30px; }
  .contact-list { list-style: none; margin-top: 26px; }
  .contact-list li {
    display: flex; align-items: center; gap: 9px;
    font-size: 15px; margin-bottom: 8px;
    white-space: nowrap;
  }
  .contact-list svg { width: 14px; height: 14px; flex: none; fill: var(--accent-orange); }
</style>
</head>
<body>

  <section class="card card-back" aria-label="Card back">
    <div class="pattern-field" role="img" aria-label="Repeating pattern of the company mark on blue"></div>
    <div class="services">
      <span>SALES</span><span class="dot"></span>
      <span>SERVICE</span><span class="dot"></span>
      <span>INSTALLATION</span><span class="dot"></span>
      <span>MAINTENANCE</span>
    </div>
    <div class="back-mark"><span class="mark-dot"></span><span>Breezeway Comfort</span></div>
  </section>

  <section class="card card-front" aria-label="Card front">
    <div class="front-brand">
      <span class="brand-dot"></span>
      <span class="brand-name">Breezeway<br>Comfort</span>
    </div>
    <div class="divider"></div>
    <div class="contact-panel">
      <h1 class="owner-name">Marcus Tollefsen</h1>
      <p class="owner-role">Owner</p>
      <p class="license">License # 2874590</p>
      <ul class="contact-list">
        <li>
          <svg viewBox="0 0 24 24" aria-hidden="true"><path d="M6.6 10.8a15.2 15.2 0 0 0 6.6 6.6l2.2-2.2c.3-.3.7-.4 1-.2 1.1.4 2.3.6 3.6.6.6 0 1 .4 1 1V20c0 .6-.4 1-1 1A17 17 0 0 1 3 4c0-.6.4-1 1-1h3.5c.6 0 1 .4 1 1 0 1.3.2 2.5.6 3.6.1.3 0 .7-.2 1z"/></svg>
          <span>555-382-4071</span>
        </li>
        <li>
          <svg viewBox="0 0 24 24" aria-hidden="true"><path d="M2 5h20v14H2zm2 2v.4l8 5.2 8-5.2V7zm0 2.8V17h16V9.8l-8 5.2z"/></svg>
          <span>breezewaycomfortair@mailvista.example</span>
        </li>
      </ul>
    </div>
  </section>

</body>
</html>
```